REDESIGN MAIN BANNER IMAGE FOR MARKETING WEBSITE

I feel like my main banner image is too busy but I like it but i want to see other options. www.brightlanepromoworks.biz I want a nice professional clean design that goes with current theme of site. Must look professional and show the variety of incentives we offer but not be overwelming.

My business is called Brightlane Promo Works and I provide businesses around the world with marketing incentives that they can use to create exciting promotions and contest and marketing giveaways to help attract more customers.

I provide a variety of different types of incentives such as Vacation Certificates, Dining Vouchers, Hotel Savings Cards, Smart Watches, Etc. that businesses can use in their marketing efforts.

I want my main banner image to reflect the variety of different categories of incentives... that I offer here: https://www.brightlanepromoworks.biz/incentives

We can use images of certificates or images.....I just want the content to be the same:

CONTENT FOR MAIN BANNER IMAGE:
INCREASE LEADS AND SALES OVERNIGHT

CREATE EXCITING MARKETING PROMOTIONS GIVING AWAY SMART DEVICES, VACATION CERTIFICATES, DINING VOUCHERS AND OTHER INCENTIVES TO YOUR CUSTOMERS

GET A FREE SAMPLE PACKAGE FOR A LIMITED TIME ONLY

Target Market(s)

b2b business owners, ceo, president, owner, founder

Industry/Entity Type

Promotional

Requirements
Must have
• Hi guys keep in mind the finished product will have to be 1800x840

Nice to have
• I want a nice professional clean design that goes with current theme of site. Must look professional and show the variety of incentives we offer but not be overwelming.
Should not have

```html
<!DOCTYPE html>
<html lang="en">
<head>
<meta charset="utf-8">
<title>Brightlane Promo Works – Increase Leads and Sales Overnight</title>
<link href="https://fonts.googleapis.com/css2?family=Michroma&family=Roboto:wght@400;500;700;900&display=swap" rel="stylesheet">
<style>
  :root{
    --blue:#1769c2;
    --ink:#171717;
    --red:#c4161c;
    --red-dark:#8e0f13;
    --green:#4fae4a;
    --green-dark:#3f9a3b;
    --navy:#0b1626;
    --floor-mid:#3a4656;
    --paper:#ffffff;
    --grey:#d9dadc;
    --text-light:#f4f6f8;
  }
  *{box-sizing:border-box;margin:0;padding:0}
  html,body{width:1200px;height:561px;overflow:hidden;background:#fff}
  .banner{
    position:relative;width:1200px;height:561px;overflow:hidden;
    background:linear-gradient(180deg,#ffffff 0,#f7f7f7 200px,#e6e7e9 296px,#c9ccd1 302px,#8d949e 340px,var(--floor-mid) 400px,#16202f 470px,var(--navy) 561px);
    font-family:"Roboto",Arial,sans-serif;
  }
  .top-rule{position:absolute;left:0;right:0;top:0;height:3px;background:linear-gradient(90deg,#b8bcc2,#e8e9eb,#b8bcc2)}
  .headline{
    position:absolute;left:0;right:0;top:84px;text-align:center;
    font-family:"Michroma","Arial Black",sans-serif;font-size:31px;letter-spacing:2.6px;
    color:var(--ink);font-weight:400;-webkit-text-stroke:1.1px currentColor;
  }
  .headline .accent{color:var(--blue)}

  .flyer-wall{position:absolute;inset:0;perspective:900px}
  .flyer{
    position:absolute;display:flex;flex-direction:column;overflow:hidden;
    background:var(--paper);box-shadow:0 3px 8px rgba(0,0,0,.35);
    font-size:var(--s);
  }
  .flyer-head{position:relative;height:30%;padding:.5em .5em 0;background:linear-gradient(160deg,#fff 55%,#e4e5e7 56%,#fff 70%,#dcdde0 71%)}
  .flyer-kicker{font-family:"Roboto",sans-serif;font-weight:900;font-size:2.3em;line-height:1;color:var(--ink);letter-spacing:-.02em}
  .flyer-title{display:inline-block;margin-top:.25em;padding:.15em .35em;background:var(--red);color:#fff;font-weight:900;font-size:1em;line-height:1.1;text-transform:uppercase}
  .flyer-logo{position:absolute;right:.5em;top:.5em;width:4.4em;height:2.6em;border:1px solid #bbb;color:#999;font-size:.8em;display:flex;align-items:center;justify-content:center;font-weight:700;letter-spacing:.05em}
  .flyer-photo{position:relative;height:25%}
  .flyer-dots{position:absolute;right:.4em;top:.3em;display:flex;flex-direction:column;gap:.3em}
  .flyer-dot{width:2.4em;height:2.4em;border-radius:50%;border:.22em solid var(--red);background:#6d7680}
  .flyer-band{background:linear-gradient(90deg,var(--red-dark),var(--red));color:#fff;font-size:.62em;font-weight:700;padding:.35em .6em;text-transform:uppercase}
  .flyer-body{flex:1;padding:.5em .6em;color:#333;font-size:.6em;line-height:1.4}
  .flyer-body b{display:block;color:var(--red);text-transform:uppercase}
  .flyer-foot{height:13%;border-top:2px solid var(--red);padding:.3em .6em;display:flex;align-items:center;justify-content:space-between;font-size:.55em;color:#444}
  .flyer-foot .url{color:var(--red);font-weight:700}

  .reflection{position:absolute;top:352px;height:60px;background:linear-gradient(180deg,rgba(255,255,255,.22),rgba(255,255,255,0));filter:blur(1px)}

  .subline{
    position:absolute;left:0;right:0;top:386px;text-align:center;color:var(--text-light);
    font-size:17.5px;line-height:19px;font-weight:400;letter-spacing:.2px;text-transform:uppercase;
  }
  .cta{position:absolute;left:390px;top:450px;width:418px;height:95px;text-decoration:none}
  .cta svg{position:absolute;inset:0}
  .cta-main{position:absolute;left:0;right:0;top:28px;text-align:center;color:#fff;font-family:"Michroma","Arial Black",sans-serif;font-size:15.5px;letter-spacing:.6px;-webkit-text-stroke:.6px #fff}
  .cta-sub{position:absolute;left:0;right:0;top:52px;text-align:center;color:#fff;font-size:11.5px;letter-spacing:.4px}
</style>
</head>
<body>
<main class="banner">
  <div class="top-rule"></div>
  <h1 class="headline"><span class="accent">INCREASE</span> LEADS AND SALES <span class="accent">OVERNIGHT</span></h1>

  <section class="flyer-wall" aria-label="Incentive certificates">
    <article class="flyer" style="left:158px;top:152px;width:130px;height:196px;--s:7.6px;transform:rotateY(16deg)">
      <div class="flyer-head"><div class="flyer-kicker">YOUR</div><div class="flyer-title">VIP Membership</div><div class="flyer-logo">LOGO</div></div>
      <div class="flyer-photo" role="img" aria-label="Photo of a pink piggy bank with coins" style="background:linear-gradient(135deg,#e9b8c4,#8c8f96)"></div>
      <div class="flyer-band">Exclusive for: customer name</div>
      <div class="flyer-body"><b>Features</b>Redeem online today</div>
      <div class="flyer-foot"><span>#10963</span><span class="url">www.perkvoucherhub.com</span></div>
    </article>

    <article class="flyer" style="left:297px;top:184px;width:113px;height:156px;--s:6.4px;transform:rotateY(10deg)">
      <div class="flyer-head"><div class="flyer-kicker">ENJOY</div><div class="flyer-title">Hotel</div><div class="flyer-logo">LOGO</div></div>
      <div class="flyer-photo" role="img" aria-label="Photo of an airliner in a blue sky" style="background:linear-gradient(180deg,#3f7fc4,#b9d6ee)"></div>
      <div class="flyer-band">Exclusive for: customer name</div>
      <div class="flyer-body"><b>Features</b>Redeem online today</div>
      <div class="flyer-foot"><span>#10963</span><span class="url">www.perkvoucherhub.com</span></div>
    </article>

    <article class="flyer" style="left:420px;top:195px;width:100px;height:135px;--s:5.6px;transform:rotateY(5deg)">
      <div class="flyer-head"><div class="flyer-kicker">DINING</div><div class="flyer-title">$100 Off</div><div class="flyer-logo">LOGO</div></div>
      <div class="flyer-photo" role="img" aria-label="Photo of wine glasses, grapes and cheese" style="background:linear-gradient(135deg,#7a3a5c,#c9a86a)"></div>
      <div class="flyer-band">Exclusive for: customer name</div>
      <div class="flyer-body"><b>Features</b>Redeem online today</div>
      <div class="flyer-foot"><span>#10963</span><span class="url">www.perkvoucherhub.com</span></div>
    </article>

    <article class="flyer" style="left:528px;top:200px;width:110px;height:128px;--s:5.4px">
      <div class="flyer-head"><div class="flyer-kicker">ENJOY</div><div class="flyer-title">Luxury Cruise</div><div class="flyer-logo">LOGO</div></div>
      <div class="flyer-photo" role="img" aria-label="Photo of a cruise ship at sea" style="background:linear-gradient(180deg,#8fc3e6,#1f5f8f)"></div>
      <div class="flyer-band">Exclusive for: customer name</div>
      <div class="flyer-body"><b>Features</b>Redeem online today</div>
      <div class="flyer-foot"><span>#10963</span><span class="url">www.perkvoucherhub.com</span></div>
    </article>

    <article class="flyer" style="left:645px;top:195px;width:105px;height:135px;--s:5.6px;transform:rotateY(-5deg)">
      <div class="flyer-head"><div class="flyer-kicker">ENJOY</div><div class="flyer-title">Earbuds</div><div class="flyer-logo">LOGO</div></div>
      <div class="flyer-photo" role="img" aria-label="Photo of wireless earbuds and a tablet" style="background:linear-gradient(135deg,#e7e1d8,#7d6a5a)"></div>
      <div class="flyer-band">Exclusive for: customer name</div>
      <div class="flyer-body"><b>Features</b>Redeem online today</div>
      <div class="flyer-foot"><span>#10963</span><span class="url">www.perkvoucherhub.com</span></div>
    </article>

    <article class="flyer" style="left:757px;top:182px;width:105px;height:158px;--s:6.2px;transform:rotateY(-10deg)">
      <div class="flyer-head"><div class="flyer-kicker">ENJOY</div><div class="flyer-title">Luxury Resort</div><div class="flyer-logo">LOGO</div></div>
      <div class="flyer-photo" role="img" aria-label="Photo of a beach resort with pools and palms" style="background:linear-gradient(180deg,#4c9fd6,#2aa39a 60%,#d9c79a)"></div>
      <div class="flyer-band">Exclusive for: customer name</div>
      <div class="flyer-body"><b>Features</b>Redeem online today</div>
      <div class="flyer-foot"><span>#10963</span><span class="url">www.perkvoucherhub.com</span></div>
    </article>

    <article class="flyer" style="left:863px;top:152px;width:177px;height:198px;--s:8px;transform:rotateY(-16deg)">
      <div class="flyer-head"><div class="flyer-kicker">ENJOY</div><div class="flyer-title">Up to 4 Nights</div><div class="flyer-logo">LOGO</div></div>
      <div class="flyer-photo" role="img" aria-label="Photo of the Las Vegas welcome sign at dusk" style="background:linear-gradient(180deg,#2c3f7a,#d4724a 70%,#3a2a2a)"></div>
      <div class="flyer-band">Exclusive for: customer name</div>
      <div class="flyer-body"><b>Features</b>Redeem online today</div>
      <div class="flyer-foot"><span>#10963</span><span class="url">www.perkvoucherhub.com</span></div>
    </article>
  </section>

  <div class="reflection" style="left:158px;width:130px"></div>
  <div class="reflection" style="left:297px;width:113px;opacity:.8"></div>
  <div class="reflection" style="left:420px;width:100px;opacity:.7"></div>
  <div class="reflection" style="left:528px;width:110px;opacity:.7"></div>
  <div class="reflection" style="left:645px;width:105px;opacity:.7"></div>
  <div class="reflection" style="left:757px;width:105px;opacity:.8"></div>
  <div class="reflection" style="left:863px;width:177px"></div>

  <p class="subline">Create exciting marketing promotions &nbsp;giving away smart devices, vacation<br>certificates, dining vouchers and other incentives to &nbsp;your customer</p>

  <a class="cta" href="https://www.brightlanepromoworks.biz/incentives">
    <svg width="418" height="95" viewBox="0 0 418 95" aria-hidden="true">
      <polygon points="4,0 414,0 418,66 209,95 0,66" fill="var(--green)"/>
      <polygon points="0,66 209,95 418,66 418,70 209,95 0,70" fill="var(--green-dark)"/>
    </svg>
    <span class="cta-main">GET A FREE SAMPLE PACKAGE</span>
    <span class="cta-sub">FOR A LIMITED TIME ONLY</span>
  </a>
</main>
</body>
</html>
```